SaaS Early tech startup business card design

Unique design for experience ecommerce platform company. the business cards will be used by executive members. conformance with color code is required.

```html
<!DOCTYPE html>
<html lang="en">
<head>
<meta charset="utf-8">
<title>nuvo business card</title>
<link href="https://fonts.googleapis.com/css2?family=Montserrat:wght@400;500;800&family=Roboto:wght@400&display=swap" rel="stylesheet">
<style>
  :root {
    --backdrop: #6c6969;
    --teal: #0f9a8c;
    --teal-deep: #1a8a8a;
    --teal-light: #22a693;
    --navy: #20223a;
    --white: #ffffff;
    --name-grey: #b9b9bd;
    --text-light: #f2f2f4;
  }
  html, body {
    margin: 0;
    padding: 0;
    width: 1200px;
    height: 1200px;
    overflow: hidden;
    background: var(--backdrop);
  }
  .canvas {
    position: relative;
    width: 1200px;
    height: 1200px;
  }
  .card {
    position: absolute;
    width: 348px;
    height: 594px;
    border-radius: 20px;
    overflow: hidden;
  }
  /* Front */
  .card-front {
    left: 200px;
    top: 298px;
  }
  .front-pattern {
    position: absolute;
    inset: 0;
    background: linear-gradient(160deg, var(--teal-deep) 0%, var(--teal) 55%, var(--teal-light) 100%);
  }
  .front-wordmark {
    position: absolute;
    left: 0;
    right: 0;
    top: 228px;
    text-align: center;
    font-family: "Montserrat", sans-serif;
    font-weight: 800;
    font-size: 94px;
    line-height: 1;
    color: var(--white);
    letter-spacing: -2px;
  }
  .front-tagline {
    position: absolute;
    left: 0;
    right: 0;
    top: 327px;
    text-align: center;
    font-family: "Montserrat", sans-serif;
    font-weight: 400;
    font-size: 15px;
    letter-spacing: 0.38em;
    color: var(--white);
    padding-left: 0.38em;
  }
  /* Back */
  .card-back {
    left: 637px;
    top: 292px;
    background: var(--navy);
  }
  .back-header {
    position: absolute;
    left: 26px;
    top: 37px;
    display: flex;
    align-items: center;
  }
  .back-tagline {
    font-family: "Montserrat", sans-serif;
    font-weight: 500;
    font-size: 16px;
    letter-spacing: 0.06em;
    color: var(--text-light);
  }
  .back-divider {
    width: 2px;
    height: 46px;
    background: var(--text-light);
    margin: 0 16px;
  }
  .back-wordmark {
    font-family: "Montserrat", sans-serif;
    font-weight: 800;
    font-size: 42px;
    line-height: 1;
    color: var(--teal-light);
  }
  .person-name {
    position: absolute;
    left: 28px;
    top: 164px;
    margin: 0;
    font-family: "Montserrat", sans-serif;
    font-weight: 800;
    font-size: 42px;
    color: var(--name-grey);
  }
  .contact-list {
    position: absolute;
    left: 30px;
    top: 233px;
    margin: 0;
    padding: 0;
    list-style: none;
    font-family: "Roboto", sans-serif;
    font-size: 17px;
    color: var(--text-light);
  }
  .contact-list li {
    display: flex;
    align-items: center;
    height: 23px;
  }
  .contact-icon {
    width: 14px;
    height: 14px;
    margin-right: 16px;
    fill: var(--teal-light);
  }
  .address {
    position: absolute;
    left: 29px;
    top: 307px;
    margin: 0;
    font-family: "Roboto", sans-serif;
    font-size: 17px;
    line-height: 24px;
    font-style: normal;
    color: var(--text-light);
  }
  .social {
    position: absolute;
    left: 29px;
    top: 518px;
    display: flex;
    flex-direction: column;
    align-items: flex-start;
    gap: 6px;
    font-family: "Roboto", sans-serif;
    font-size: 17px;
    line-height: 20px;
    color: var(--text-light);
  }
  .social-dot {
    width: 14px;
    height: 14px;
    border-radius: 50%;
    background: var(--teal-light);
  }
  .back-pattern {
    position: absolute;
    right: 0;
    bottom: 0;
    width: 126px;
    height: 152px;
    border-top-left-radius: 30px;
    background: linear-gradient(150deg, rgba(34,166,147,0.05) 0%, rgba(34,166,147,0.35) 100%);
  }
</style>
</head>
<body>
<main class="canvas">
  <section class="card card-front" aria-label="Card front">
    <div class="front-pattern" role="img" aria-label="Teal background with overlapping ribbon line pattern"></div>
    <div class="front-wordmark">nuvo</div>
    <div class="front-tagline">SIMPLY YOUR OWN</div>
  </section>

  <section class="card card-back" aria-label="Card back">
    <header class="back-header">
      <span class="back-tagline">Simply your own</span>
      <span class="back-divider"></span>
      <span class="back-wordmark">nuvo</span>
    </header>

    <h1 class="person-name">Karim D.</h1>

    <ul class="contact-list">
      <li>
        <svg class="contact-icon" viewBox="0 0 16 16" aria-hidden="true">
          <path d="M1 5c0-2 3-3 7-3s7 1 7 3v1.5h-3.5V5h-7v1.5H1z"/>
          <path d="M3 8h10l1 6H2z"/>
        </svg>
        (00) 0123 NUVO
      </li>
      <li>
        <svg class="contact-icon" viewBox="0 0 16 16" aria-hidden="true">
          <path d="M1 3h14v10H1z M2.5 4.5 8 9l5.5-4.5" fill="none" stroke="#22a693" stroke-width="1.6"/>
        </svg>
        hello@nuvo.net
      </li>
      <li>
        <svg class="contact-icon" viewBox="0 0 16 16" aria-hidden="true">
          <g fill="none" stroke="#22a693" stroke-width="1.3">
            <circle cx="8" cy="8" r="6.5"/>
            <ellipse cx="8" cy="8" rx="3" ry="6.5"/>
            <path d="M1.5 8h13M2.5 4.8h11M2.5 11.2h11"/>
          </g>
        </svg>
        www.nuvo.net
      </li>
    </ul>

    <address class="address">Lumen Tower, Dubai<br>Harbor Tech Park, UAE</address>

    <div class="social">
      <span class="social-dot"></span>
      <span>/getnuvo</span>
    </div>

    <div class="back-pattern" role="img" aria-label="Corner ribbon line pattern in teal"></div>
  </section>
</main>
</body>
</html>
```